Modern Billboard Ad for Criminal Defense Firm

10.5 x 36 We're looking for something to set us apart from the local competition. Looking for sleek and modern. We're a mid-sized firm in a small market city. We want to give the artist room to be creative on this one.
Thanks

Target Market(s)

Adult clients who have been charged with a crime/DWI

Industry/Entity Type

legal

Font styles to use
Serif
Sans Serif

Requirements
Must have
• Needs to have the firm name in large lettering. Law Offices of Marcus T Whitfield. “PLLC” does not have to be included. Phone number of (555) 384-1927 should be included but not the main focus.
Nice to have
• A call to action or something similar. “Don’t go it alone, call today.”, “ Arrested?”

```html
<!DOCTYPE html>
<html lang="en">
<head>
<meta charset="utf-8">
<title>Law Offices of Marcus T Whitfield – Billboard</title>
<link rel="stylesheet" href="https://fonts.googleapis.com/css2?family=Oswald:wght@600;700&family=Arimo:wght@700&display=swap">
<style>
  :root {
    --canvas: #e4e6e8;
    --white: #ffffff;
    --teal: #2f8f9a;
    --teal-deep: #1f6f79;
    --teal-shadow: #0f4950;
    --sky-top: #3c98a6;
    --sky-bottom: #a6dbe4;
    --navy: #131a6b;
    --pill-start: #2a8793;
    --pill-end: #4fc3dd;
    --icon-dark: #0f1a1f;
    --photo-light: #9fa9ad;
    --photo-mid: #6f7a7e;
    --photo-dark: #4a5457;
    --badge-dark: #1b2a4a;
    --badge-blue: #2ea8df;
  }
  * { box-sizing: border-box; margin: 0; padding: 0; }
  html, body {
    width: 1200px; height: 1200px; overflow: hidden;
    background: var(--canvas);
  }
  .canvas {
    position: relative; width: 1200px; height: 1200px;
    display: flex; align-items: center; justify-content: center;
  }
  .billboard {
    position: relative; width: 1120px; height: 327px;
    background: var(--white); overflow: hidden;
    box-shadow: 0 6px 24px rgba(0,0,0,.18);
  }
  .sky-panel {
    position: absolute; top: 0; right: 0; bottom: 0; left: 560px;
    background: linear-gradient(180deg, var(--sky-top) 0%, #6cbac7 55%, var(--sky-bottom) 100%);
  }
  .portrait {
    position: absolute; left: 400px; top: 0; width: 410px; height: 327px;
    background: radial-gradient(ellipse 60% 75% at 50% 60%, var(--photo-light) 0%, var(--photo-mid) 60%, var(--photo-dark) 100%);
    -webkit-mask-image: linear-gradient(90deg, transparent 0%, #000 12%, #000 88%, transparent 100%);
            mask-image: linear-gradient(90deg, transparent 0%, #000 12%, #000 88%, transparent 100%);
  }
  .headline-lead {
    position: absolute; left: 40px; top: 96px;
    font-family: "Oswald", "Arial Narrow", sans-serif; font-weight: 700;
    font-size: 66px; line-height: 1; letter-spacing: -0.5px;
    color: var(--teal); white-space: nowrap;
    text-shadow: 2px 2px 0 var(--teal-deep), 4px 4px 0 var(--teal-shadow), 6px 7px 6px rgba(0,0,0,.35);
    transform: scaleX(0.92); transform-origin: left center;
  }
  .tagline {
    position: absolute; left: 36px; top: 192px;
    font-family: "Arimo", Arial, sans-serif; font-weight: 700;
    font-size: 17px; color: var(--navy); white-space: nowrap;
  }
  .phone-pill {
    position: absolute; left: 30px; top: 238px;
    width: 346px; height: 52px; border-radius: 26px;
    background: linear-gradient(90deg, var(--pill-start), var(--pill-end));
    display: flex; align-items: center; gap: 12px; padding-left: 12px;
  }
  .phone-icon { width: 34px; height: 34px; flex: none; }
  .phone-number {
    font-family: "Arimo", Arial, sans-serif; font-weight: 700;
    font-size: 31px; color: var(--white); letter-spacing: .5px;
  }
  .headline-name {
    position: absolute; right: 26px; top: 36px; z-index: 2;
    font-family: "Oswald", "Arial Narrow", sans-serif; font-weight: 700;
    font-size: 54px; line-height: 1; letter-spacing: 0.5px;
    color: var(--white); white-space: nowrap;
    text-shadow: 2px 2px 0 #c9d3d6, 4px 4px 0 #8d9a9e, 6px 7px 6px rgba(0,0,0,.4);
  }
  .award-badge {
    position: absolute; left: 878px; top: 140px; width: 72px; height: 110px;
    border-radius: 4px;
    background: linear-gradient(180deg, var(--badge-blue) 0%, var(--badge-dark) 45%, var(--badge-dark) 100%);
    border: 3px solid var(--white);
    box-shadow: 3px 4px 8px rgba(0,0,0,.3);
  }
</style>
</head>
<body>
<main class="canvas">
  <section class="billboard" aria-label="Billboard for Law Offices of Marcus T Whitfield">
    <div class="sky-panel"></div>

    <div class="portrait" role="img" aria-label="Portrait photograph of the attorney in a vest and tie, jacket over his shoulder"></div>

    <h1 class="headline-lead">LAW OFFICES OF</h1>
    <p class="tagline">“Don’t go it alone, call today.”, “ Arrested?”</p>

    <div class="phone-pill">
      <svg class="phone-icon" viewBox="0 0 34 34" aria-hidden="true">
        <circle cx="17" cy="17" r="16" fill="var(--icon-dark)" stroke="var(--white)" stroke-width="1.5"/>
        <path d="M12.5 9.5c.8-.6 1.8-.4 2.3.4l1.4 2.4c.4.7.2 1.6-.4 2.1l-1 .8c.8 1.9 2.2 3.4 4.1 4.3l.8-1c.5-.6 1.4-.8 2.1-.4l2.4 1.4c.8.5 1 1.5.4 2.3l-.9 1.2c-.7.9-1.9 1.2-3 .8-4.5-1.6-8-5.1-9.5-9.6-.4-1.1 0-2.3.8-3z" fill="var(--white)"/>
      </svg>
      <span class="phone-number">(555) 384-1927</span>
    </div>

    <h2 class="headline-name">MARCUS T WHITFIELD</h2>

    <div class="award-badge" role="img" aria-label="Community award badge"></div>
  </section>
</main>
</body>
</html>
```